Medigap Insurance Interactive website

We are looking at redesigning our website for a more up to date and responsive look and feel. We will code this site using Bootstrap 3 so please research and know how to design for this. Attached is our logo and a wireframe for the new site.
I look forward to seeing what you guys can do.

Target Market(s)

People elegible for Medigap Insurance in the US

Industry/Entity Type

Insurance

Number of Pages Required

5+ page

Font styles to use
Sans Serif

Requirements
Must have
• Match the logo
• Be Bootstrap 3 compatible design
• Font Awesome Icons

```html
<!DOCTYPE html>
<html lang="en">
<head>
<meta charset="utf-8">
<title>PlanBridge – Medicare Supplement Plans</title>
<link rel="stylesheet" href="https://fonts.googleapis.com/css2?family=Open+Sans:wght@300;400;600&display=swap">
<style>
:root{
  --red:#b41f1a;
  --navy:#12295c;
  --blue:#0f73c8;
  --green:#06962c;
  --yellow:#f4bb1d;
  --text:#555;
  --muted:#777;
  --footer:#07142a;
  --border:#d9d9d9;
}
*{box-sizing:border-box;margin:0;padding:0}
html,body{width:1200px;height:972px;overflow:hidden;background:#fff;font-family:"Open Sans",Arial,sans-serif;color:var(--text)}
.page{position:relative;width:1200px;height:972px}
.site-header{position:absolute;top:0;left:0;width:1200px;height:92px;border-top:3px solid var(--red);background:#fff}
.brand{position:absolute;left:99px;top:30px;font-size:21px;font-weight:400;color:var(--red);letter-spacing:.5px}
.brand-mark{display:inline-block;width:10px;height:10px;border-radius:50%;background:var(--navy);margin-left:6px;vertical-align:middle}
.header-contact{position:absolute;right:187px;top:22px;font-size:13.5px;color:#444;font-weight:400}
.social{position:absolute;right:113px;top:26px;display:flex;gap:8px}
.social span{width:11px;height:11px;border-radius:50%;background:#555;display:block}
.main-nav{position:absolute;right:99px;top:52px;display:flex;gap:34px;font-size:13px;color:#555}
.hero{position:absolute;top:92px;left:0;width:1200px;height:470px;background:radial-gradient(ellipse at 50% 40%,#7a6e6a 0%,#55504f 50%,#3e3b3c 100%)}
.hero-arrow{position:absolute;top:195px}
.hero-arrow.left{left:40px}
.hero-arrow.right{right:40px}
.slide{position:absolute;top:82px;height:307px;border:3px solid #fff}
.slide-insure{left:99px;width:547px;background:linear-gradient(120deg,#0a1b2c 0%,#0d3a56 45%,#0fa7c9 70%,#0b2a3d 100%)}
.slide-insure .caption{position:absolute;left:34px;bottom:38px;color:#fff}
.caption h2{font-size:30px;font-weight:600;letter-spacing:.5px}
.caption p{font-size:21px;font-weight:400;margin-top:8px}
.slide-video{left:662px;width:439px;background:linear-gradient(90deg,#d8d4d2 0%,#9d8c82 45%,#6e6a6d 70%,#b08f72 100%)}
.play{position:absolute;left:50%;top:50%;width:100px;height:100px;margin:-53px 0 0 -56px;border-radius:50%;background:rgba(40,40,40,.75);display:flex;align-items:center;justify-content:center}
.actions{position:absolute;top:562px;left:0;width:1200px;height:83px;display:flex}
.action{flex:1;display:flex;align-items:center;justify-content:center;gap:14px;color:#fff;font-size:18px;font-weight:400;letter-spacing:.3px}
.action.compare{background:var(--blue)}
.action.buy{background:var(--red)}
.action.learn{background:var(--green)}
.action.help{background:var(--yellow)}
.section-title{font-size:22px;font-weight:400;display:inline-block;position:relative}
.section-title .r{color:var(--red)}
.section-title .b{color:var(--navy)}
.underline{display:flex;gap:6px;margin-top:4px}
.underline i{display:block;height:2px}
.col{position:absolute;top:688px}
.col-about{left:98px;width:305px}
.col-about p{font-size:12.3px;font-weight:300;line-height:19.6px;text-align:justify;margin-top:18px;color:#666}
.col-quotes{left:466px;width:285px}
.col-quotes blockquote{font-size:12.3px;font-weight:300;line-height:20.5px;margin-top:18px;color:#666}
.author{position:relative;height:62px;margin-top:4px}
.author .nav{position:absolute;left:0;top:29px;display:flex;gap:4px}
.author .nav span{width:15px;height:15px;border-radius:50%;background:#ccc}
.author .name{position:absolute;left:78px;top:18px;font-size:14px;color:#333;font-weight:600;line-height:18px}
.author .name small{display:block;font-size:12.5px;font-weight:400;color:#444}
.avatar{position:absolute;right:0;top:0;width:60px;height:60px;border-radius:50%;border:2px solid var(--red);background:radial-gradient(circle at 50% 40%,#d7b49b 0%,#8ea7c4 70%)}
.col-updates{left:823px;width:279px}
.email{margin-top:24px;height:38px;border:1px solid var(--border);background:#f3f3f3;font-size:14px;color:#aaa;padding:9px 16px}
.signup{margin-top:9px;height:37px;background:var(--red);color:#fff;font-size:16px;text-align:center;line-height:37px;border:1px solid #9a1712}
.updates-note{font-size:10.5px;color:#555;text-align:center;margin-top:8px}
.site-footer{position:absolute;left:0;top:906px;width:1200px;height:66px;background:var(--footer);color:#7d8494}
.footer-links{position:absolute;left:97px;top:22px;font-size:14px;font-weight:400}
.footer-links span{margin:0 10px}
.copyright{position:absolute;right:99px;top:24px;font-size:12px}
</style>
</head>
<body>
<div class="page">
  <header class="site-header">
    <div class="brand">PLANBRIDGE<span class="brand-mark"></span></div>
    <div class="header-contact">Compare Rates &amp; Save (800)555 - 0142</div>
    <div class="social"><span></span><span></span><span></span><span></span></div>
    <nav class="main-nav">
      <span>Medicare Supplement</span><span>Part D</span><span>How To Decide</span><span>Learn Online</span><span>Why PlanBridge</span><span>Buy Now</span>
    </nav>
  </header>

  <section class="hero" role="img" aria-label="Blurred photo of hands sheltering a toy car">
    <svg class="hero-arrow left" width="24" height="70" viewBox="0 0 24 70"><path d="M22 2 L2 35 L22 68" fill="none" stroke="#ddd" stroke-width="1.5"/></svg>
    <svg class="hero-arrow right" width="24" height="70" viewBox="0 0 24 70"><path d="M2 2 L22 35 L2 68" fill="none" stroke="#ddd" stroke-width="1.5"/></svg>
    <div class="slide slide-insure" role="img" aria-label="Hand touching glowing insurance icons for home, car, health, travel and family">
      <div class="caption"><h2>WHY US ?</h2><p>WE ARE PLANBRIDGE</p></div>
    </div>
    <div class="slide slide-video" role="img" aria-label="Video still of a smiling couple shaking hands with an advisor">
      <div class="play"><svg width="14" height="16" viewBox="0 0 14 16"><path d="M1 1 L13 8 L1 15Z" fill="#fff"/></svg></div>
    </div>
  </section>

  <section class="actions">
    <div class="action compare">
      <svg width="26" height="26" viewBox="0 0 26 26"><circle cx="13" cy="13" r="12" fill="#fff"/><text x="13" y="18" text-anchor="middle" font-size="13" font-weight="600" fill="#0f73c8" font-family="Open Sans,sans-serif">%</text></svg>
      <span>COMPARE RATES</span></div>
    <div class="action buy">
      <svg width="28" height="26" viewBox="0 0 28 26"><path d="M1 4h4l4 14h14l3-10H7" fill="none" stroke="#fff" stroke-width="2"/><circle cx="11" cy="22" r="2" fill="#fff"/><circle cx="21" cy="22" r="2" fill="#fff"/><path d="M16 2v8M13 7l3 3 3-3" stroke="#fff" stroke-width="2" fill="none"/></svg>
      <span>BUY NOW</span></div>
    <div class="action learn">
      <svg width="28" height="24" viewBox="0 0 28 24"><rect x="1" y="1" width="14" height="14" fill="none" stroke="#fff" stroke-width="2"/><rect x="11" y="8" width="16" height="15" fill="#fff"/><text x="19" y="20" text-anchor="middle" font-size="11" font-weight="600" fill="#06962c" font-family="Open Sans,sans-serif">A</text></svg>
      <span>LEARN ONLINE</span></div>
    <div class="action help">
      <svg width="28" height="28" viewBox="0 0 28 28"><path d="M5 8c0 8 7 16 15 16l3-4-4-3-3 2c-3-2-5-4-7-7l2-3-3-4z" fill="#fff"/><circle cx="19" cy="8" r="7" fill="#fff"/><rect x="18" y="7" width="2" height="5" fill="#f4bb1d"/><rect x="18" y="4" width="2" height="2" fill="#f4bb1d"/></svg>
      <span>GET EXPERT HELP</span></div>
  </section>

  <section class="col col-about">
    <h3 class="section-title"><span class="r">PLANBRIDGE</span></h3>
    <div class="underline"><i style="width:108px;background:var(--red)"></i><i style="width:34px;background:var(--navy)"></i></div>
    <p>It is a long established fact that a reader will be distracted by the readable content of a page when looking at its layout. The point of using Lorem Ipsum is that it has a more-or-less normal distribution of letters, as opposed to using 'Content here, content here', making it look like readable English.</p>
  </section>

  <section class="col col-quotes">
    <h3 class="section-title"><span class="r">WHAT PEOPLE ARE </span><span class="b">SAYING</span></h3>
    <div class="underline"><i style="width:190px;background:var(--red)"></i><i style="width:76px;background:var(--navy)"></i></div>
    <blockquote>"Lorem ipsum dolor sit amet, consectetur adipiscing elit, sed do eiusmod tempor &nbsp;incididunt ut labore et dolore magna aliqua"</blockquote>
    <div class="author">
      <div class="nav"><span></span><span></span></div>
      <div class="name">Finibus Bonorum et<small>Direct Manager</small></div>
      <div class="avatar" role="img" aria-label="Portrait of the reviewer"></div>
    </div>
  </section>

  <section class="col col-updates">
    <h3 class="section-title"><span class="r">MONTHLY </span><span class="b">UPDATES</span></h3>
    <div class="underline"><i style="width:100px;background:var(--red)"></i><i style="width:92px;background:var(--navy)"></i></div>
    <div class="email">Email Address</div>
    <div class="signup">SIGN UP</div>
    <div class="updates-note">Enter Email for customized monthly rate updates &amp; more</div>
  </section>

  <footer class="site-footer">
    <div class="footer-links">PlanBridge<span>|</span>Sitemap<span>|</span>Buy Now<span>|</span>Blog<span>|</span>Login</div>
    <div class="copyright">Copyrights@2016 Company Name , All rights reserved</div>
  </footer>
</div>
</body>
</html>
```